Corporate Letterhead

Looking for a new corporate letterhead design. Our colors are orange and gray.

We'd like it if the below could be included somehow in the letterhead.                                       

Partnerships | Results | Quality

• Logo, Company Name, Address, Phone #, Fax #, Web address, Email address (optional), the phrase "A Service Disable Veteran Owned Small Business".

```html
<!DOCTYPE html>
<html lang="en">
<head>
<meta charset="utf-8">
<title>Corvane Technology, Inc — Letterhead</title>
<link href="https://fonts.googleapis.com/css2?family=Arimo:wght@400&family=Michroma&display=swap" rel="stylesheet">
<style>
  :root {
    --backdrop: #c9c9c9;
    --paper: #ffffff;
    --orange: #f39422;
    --gray: #8a8a8a;
    --ink: #1e1e1e;
    --signature: #ececec;
  }
  * { box-sizing: border-box; margin: 0; padding: 0; }
  html, body { width: 1200px; height: 847px; overflow: hidden; background: var(--backdrop); }
  .letterhead {
    position: absolute; left: 291px; top: 24px;
    width: 618px; height: 800px;
    background: var(--paper);
    box-shadow: 0 2px 10px rgba(0,0,0,.18);
    font-family: "Arimo", Arial, sans-serif;
    color: var(--ink);
  }
  .tagline {
    position: absolute; left: 48px; top: 40px;
    padding-left: 12px;
    border-left: 5px solid var(--orange);
    font-family: "Michroma", sans-serif;
    font-size: 7.5px; line-height: 10px; letter-spacing: .5px;
    color: var(--gray);
  }
  .brand {
    position: absolute; right: 48px; top: 44px;
    display: flex; align-items: center; gap: 8px;
  }
  .brand-dot { width: 14px; height: 14px; border-radius: 50%; background: var(--orange); }
  .brand-name {
    font-family: "Michroma", sans-serif;
    font-size: 14px; color: var(--orange); letter-spacing: .5px;
  }
  .letter-body {
    position: absolute; left: 64px; right: 64px; top: 112px;
    font-size: 8.4px; line-height: 13px;
  }
  .salutation { margin-bottom: 10px; }
  .letter-body p.para { text-align: justify; margin-bottom: 13px; }
  .signoff { position: absolute; right: 64px; top: 560px; font-size: 8px; line-height: 11px; }
  .signature { width: 110px; height: 26px; background: var(--signature); margin-bottom: 6px; border-radius: 3px; }
  .footer {
    position: absolute; left: 48px; bottom: 40px;
    padding-left: 12px;
    border-left: 5px solid var(--orange);
    font-family: "Michroma", sans-serif;
    font-size: 7.5px; line-height: 10px; letter-spacing: .4px;
    color: var(--gray);
  }
  .footer-name { color: var(--orange); font-size: 9.5px; line-height: 12px; }
  .footer-contacts { display: flex; gap: 10px; margin-top: 3px; }
  .footer-contacts .phones span { color: var(--orange); }
  .footer-contacts .online { border-left: 1px solid var(--orange); padding-left: 8px; }
</style>
</head>
<body>
  <article class="letterhead">
    <div class="tagline">PARTNERSHIPS<br>RESULTS<br>QUALITY</div>

    <div class="brand">
      <span class="brand-dot"></span>
      <span class="brand-name">CORVANE TECHNOLOGY, INC</span>
    </div>

    <section class="letter-body">
      <p class="salutation">Dear Client,</p>
      <p class="para">Lorem ipsum dolor sit amet, consectetur adipisicing elit, sed do eiusmod tempor incididunt ut labore et dolore magna aliqua. Ut enim ad minim veniam, quis nostrud exercitation ullamco laboris nisi ut aliquip ex ea commodo consequat. Duis aute irure dolor in reprehenderit in voluptate velit esse cillum dolore eu fugiat nulla pariatur. Excepteur sint occaecat cupidatat non proident, sunt in culpa qui officia deserunt mollit anim id est laborum.</p>
      <p class="para">Lorem ipsum dolor sit amet, consectetur adipisicing elit, sed do eiusmod tempor incididunt ut labore et dolore magna aliqua. Ut enim ad minim veniam, quis nostrud exercitation ullamco laboris nisi ut aliquip ex ea commodo consequat. Duis aute irure dolor in reprehenderit in voluptate velit esse cillum dolore eu fugiat nulla pariatur. Excepteur sint occaecat cupidatat non proident, sunt in culpa qui officia deserunt mollit anim id est laborum.</p>
      <p class="para">Lorem ipsum dolor sit amet, consectetur adipisicing elit, sed do eiusmod tempor incididunt ut labore et dolore magna aliqua. Ut enim ad minim veniam, quis nostrud exercitation ullamco laboris nisi ut aliquip ex ea commodo consequat. Duis aute irure dolor in reprehenderit in voluptate velit esse cillum dolore eu fugiat nulla pariatur. Excepteur sint occaecat cupidatat non proident, sunt in culpa qui officia deserunt mollit anim id est laborum.</p>
      <p class="para">Lorem ipsum dolor sit amet, consectetur adipisicing elit, sed do eiusmod tempor incididunt ut labore et dolore magna aliqua. Ut enim ad minim veniam, quis nostrud exercitation ullamco laboris nisi ut aliquip ex ea commodo consequat. Duis aute irure dolor in reprehenderit in voluptate velit esse cillum dolore eu fugiat nulla pariatur. Excepteur sint occaecat cupidatat non proident, sunt in culpa qui officia deserunt mollit anim id est laborum.</p>
      <p class="para">Lorem ipsum dolor sit amet, consectetur adipisicing elit, sed do eiusmod tempor incididunt ut labore et dolore magna aliqua. Ut enim ad minim veniam, quis nostrud exercitation ullamco laboris nisi ut aliquip ex ea.</p>
    </section>

    <div class="signoff">
      <div class="signature" role="img" aria-label="Handwritten signature of Daniel Reyes"></div>
      <div>Daniel Reyes</div>
      <div>Executive manager</div>
    </div>

    <footer class="footer">
      <div class="footer-name">CORVANE TECHNOLOGY, INC</div>
      <div>4120 COMMERCE DRIVE | SUITE 210 | HANOVER, MD 21076</div>
      <div class="footer-contacts">
        <div class="phones"><span>P:</span> 443.555.0142<br><span>F:</span> 410.555.0187</div>
        <div class="online">INFO@CORVANETECHINC.COM<br>WWW.CORVANETECHINC.COM</div>
      </div>
    </footer>
  </article>
</body>
</html>
```